Online Marketing Agency Website

We are an online marketing agency that specializes in search marketing (SEM) for businesses of all sizes. Our core services include local search marketing, seo, paid search, paid social, graphic design, video production/editing and website design. We have an existing website that we launched a number of years ago but it's very outdated and we're currently too busy to design a new version.

Target Market(s)

Any business that needs online marketing services with an emphasis on search marketing.

Industry/Entity Type

Ad Agency

Number of Pages Required

4 page

Font styles to use
Sans Serif

Requirements
Must have
• Home page, interior page, blog page, contact us page.
Look and feel should be modern and clean and easy to navigate.
Sections for call outs for specific services: Business Marketing Strategy, Content Creation and Marketing, Graphic & Publication Design, Pay Per Click (PPC) Management, Search Engine Optimization, Social Media Management, Video Production & Editing, Website Hosting & Management, Website Design & Development
Use color from logo that was uploaded.

```html
<!DOCTYPE html>
<html lang="en">
<head>
<meta charset="utf-8">
<title>Apex Reach – Search Marketing Made Simple</title>
<link href="https://fonts.googleapis.com/css2?family=Roboto:wght@300;400;500;700;900&display=swap" rel="stylesheet">
<style>
:root{
  --orange:#f05a22;
  --orange-deep:#e0461a;
  --orange-soft:#f7a27f;
  --ink:#1d1d1d;
  --text:#333333;
  --muted:#6b6b6b;
  --card:#f6f6f6;
  --footer:#1c1c1c;
  --white:#ffffff;
}
*{margin:0;padding:0;box-sizing:border-box}
html,body{width:1200px;height:4804px;overflow:hidden}
body{position:relative;font-family:"Roboto",Arial,sans-serif;color:var(--text);background:var(--white)}
.abs{position:absolute}
.btn{position:absolute;display:flex;align-items:center;justify-content:center;border-radius:19px;background:var(--orange);color:var(--white);font-size:15px;font-weight:500;box-shadow:0 4px 8px rgba(240,90,34,.35)}
.btn-outline{background:var(--white);color:var(--orange);border:2px solid var(--orange);box-shadow:none}
.btn-dark{background:#111;box-shadow:0 4px 8px rgba(0,0,0,.3)}
.section-title{position:absolute;font-size:31px;font-weight:700;color:var(--ink);letter-spacing:.5px}
.section-title span{color:var(--orange)}
.lead{position:absolute;font-size:14.5px;line-height:19px;text-align:center;color:var(--text)}

/* hero */
.hero{left:0;top:0;width:1200px;height:612px;overflow:hidden}
.hero-photo{position:absolute;inset:0;background:linear-gradient(120deg,#3a2a22 0%,#5a4335 35%,#2f2925 65%,#4a3a30 100%)}
.hero-shade{position:absolute;inset:0;background:rgba(20,14,10,.45)}
.nav-link{position:absolute;top:98px;font-size:15px;font-weight:700;color:var(--white);letter-spacing:.3px}
.nav-rule{position:absolute;top:130px;height:2px;background:var(--orange)}
.social{position:absolute;width:20px;height:20px;border:2px solid var(--orange);border-radius:50%}
.brand-mark{position:absolute;width:34px;height:34px;border-radius:50%;background:var(--orange)}
.brand-name{position:absolute;font-weight:700;letter-spacing:.5px;white-space:nowrap;text-align:center}
.brand-tag{position:absolute;white-space:nowrap;text-align:center}
.hero-title{left:0;width:1200px;top:244px;text-align:center;font-size:42px;font-weight:300;color:var(--orange)}
.hero-sub{left:0;width:1200px;top:318px;text-align:center;font-size:20px;line-height:25px;color:var(--white)}
.dot{position:absolute;width:10px;height:10px;border-radius:50%;background:#cfcfcf}
.dot.active{width:18px;border-radius:5px;background:var(--white)}

/* who */
.who-text{left:174px;top:782px;width:380px;font-size:13.6px;line-height:19px;color:var(--text)}
.who-art{left:662px;top:690px;width:476px;height:327px;border-radius:8px;background:radial-gradient(circle at 60% 45%,#fde3d7 0%,#f5f0ec 55%,#ffffff 100%)}
.divider{position:absolute;height:2px;background:linear-gradient(90deg,transparent,var(--orange-soft) 30%,var(--orange-soft) 70%,transparent)}

/* services */
.service{position:absolute;width:168px;height:168px;border-radius:30px;background:var(--card);box-shadow:0 6px 12px rgba(0,0,0,.08);display:flex;flex-direction:column;align-items:center}
.service svg{margin-top:22px}
.service p{margin-top:14px;font-size:14.5px;font-weight:500;line-height:19px;text-align:center;color:var(--ink)}

/* featured */
.featured-band{left:0;top:1814px;width:1200px;height:328px;background:linear-gradient(90deg,var(--orange-deep),var(--orange) 60%,#f26a33)}
.work{position:absolute;box-shadow:0 6px 14px rgba(0,0,0,.25)}
.work-caption{position:absolute;left:0;right:0;text-align:center;color:var(--white)}

/* blogs */
.blog-img{position:absolute;width:254px;height:195px}
.blog-title{position:absolute;width:260px;font-size:16px;font-weight:700;line-height:21px;color:var(--ink)}
.blog-text{position:absolute;width:224px;font-size:14px;line-height:19px;text-align:justify;color:var(--text)}

/* contact */
.doodle{position:absolute;border-radius:40px;background:radial-gradient(circle,#f0f0f0 0%,#fafafa 60%,#ffffff 100%)}
.form-box{left:243px;top:3428px;width:714px;height:632px;border-radius:0 70px 70px 70px;background:linear-gradient(160deg,#f36d35,var(--orange) 50%,var(--orange-deep))}
.label{position:absolute;font-size:12px;color:var(--white)}
.field{position:absolute;height:44px;background:var(--white);border-radius:4px}

/* footer */
.footer{left:0;top:4154px;width:1200px;height:650px;background:var(--footer)}
.foot-head{position:absolute;top:4410px;font-size:15px;font-weight:500;color:#e6e6e6;letter-spacing:.3px}
.foot-link{position:absolute;font-size:14px;color:#d8d8d8}
</style>
</head>
<body>

<!-- HERO -->
<section class="abs hero">
  <div class="hero-photo" role="img" aria-label="Overhead photo of a team working at a wooden desk with laptops, tablets and phones"></div>
  <div class="hero-shade"></div>
  <svg class="abs" style="left:0;top:0" width="1200" height="612">
    <polygon points="0,520 0,612 1200,612 1200,560 640,580" fill="#e0461a" opacity=".9"/>
    <polygon points="0,560 0,612 700,612" fill="#f05a22"/>
  </svg>

  <div class="social" style="left:107px;top:42px"></div>
  <div class="social" style="left:153px;top:42px"></div>
  <div class="social" style="left:199px;top:42px"></div>
  <div class="social" style="left:245px;top:42px"></div>

  <div class="btn" style="left:948px;top:32px;width:134px;height:37px;font-size:15px">CONTACT</div>

  <div class="brand-mark" style="left:583px;top:30px"></div>
  <div class="brand-name" style="left:480px;width:240px;top:98px;font-size:21px;color:#e9e9e9">APEX REACH</div>
  <div class="brand-tag" style="left:480px;width:240px;top:121px;font-size:12px;color:#dcdcdc">Search Marketing Made Simple</div>

  <div class="nav-link" style="left:128px">HOME</div>
  <svg class="abs" style="left:142px;top:122px" width="12" height="8"><polygon points="6,0 12,8 0,8" fill="#f05a22"/></svg>
  <div class="nav-link" style="left:238px">ABOUT</div>
  <div class="nav-link" style="left:342px">SERVICES</div>
  <div class="nav-link" style="left:782px">FEATURED WORK</div>
  <div class="nav-link" style="left:985px">BLOG</div>
  <div class="nav-rule" style="left:0;width:510px"></div>
  <div class="nav-rule" style="left:712px;width:488px"></div>

  <h1 class="abs hero-title">Local SEO &amp; Business Listings</h1>
  <p class="abs hero-sub">85% of Consumers Use the Internet to Find Local<br>Businesses Are They Finding Yours?</p>
  <div class="btn" style="left:534px;top:400px;width:132px;height:38px">EXPLORE</div>

  <svg class="abs" style="left:115px;top:365px" width="62" height="36"><path d="M60 18H4M20 2L4 18l16 16" stroke="#fff" stroke-width="2.5" fill="none"/></svg>
  <svg class="abs" style="left:1023px;top:365px" width="62" height="36"><path d="M2 18h56M42 2l16 16-16 16" stroke="#fff" stroke-width="2.5" fill="none"/></svg>

  <div class="dot active" style="left:570px;top:570px"></div>
  <div class="dot" style="left:597px;top:570px"></div>
  <div class="dot" style="left:618px;top:570px"></div>
</section>

<!-- WHO WE ARE -->
<h2 class="section-title" style="left:174px;top:708px"><span>WHO</span> WE ARE</h2>
<p class="abs who-text">Apex Reach is a full-service online marketing agency. We can handle any element of your online marketing so you can get back to doing what you do best – growing your business. All of our services are offered on an 'a la carte' basis Apex Reach is a full-service online marketing agency.We can handle</p>
<div class="btn" style="left:175px;top:950px;width:133px;height:37px">Read More</div>
<div class="abs who-art" role="img" aria-label="Smiling woman with glasses working at a laptop in front of a large orange triangle"></div>
<div class="divider" style="left:140px;top:1056px;width:513px"></div>

<!-- SERVICES -->
<h2 class="section-title" style="left:0;width:1200px;text-align:center;top:1113px"><span>OUR</span> SERVICES</h2>
<p class="lead" style="left:350px;width:500px;top:1174px">Apex Reach is a full-service online marketing agency. We can handle any element of your</p>

<div class="service" style="left:179px;top:1271px">
  <svg width="52" height="52" viewBox="0 0 52 52" fill="none" stroke="#f05a22" stroke-width="2"><circle cx="34" cy="16" r="12"/><circle cx="34" cy="16" r="6"/><path d="M34 16L14 30M6 40h22l6 8H10z"/></svg>
  <p>Business<br>Marketing Strategy</p>
</div>
<div class="service" style="left:403px;top:1271px">
  <svg width="52" height="52" viewBox="0 0 52 52" fill="none" stroke="#f05a22" stroke-width="2"><circle cx="26" cy="8" r="4"/><path d="M26 12v8M8 20h36M26 20l-8 18h16zM26 38v10"/><circle cx="8" cy="20" r="3"/><circle cx="44" cy="20" r="3"/></svg>
  <p>Graphic &amp;<br>Publication Design</p>
</div>
<div class="service" style="left:627px;top:1271px">
  <svg width="52" height="52" viewBox="0 0 52 52" fill="none" stroke="#f05a22" stroke-width="2"><rect x="6" y="6" width="40" height="28" rx="2"/><path d="M12 14h28M12 20h20M12 26h24M20 34l-4 14h20l-4-14"/></svg>
  <p>Content Creation<br>and Marketing</p>
</div>
<div class="service" style="left:851px;top:1271px">
  <svg width="52" height="52" viewBox="0 0 52 52" fill="none" stroke="#f05a22" stroke-width="2"><rect x="4" y="6" width="44" height="36" rx="2"/><path d="M4 14h44M12 36V28M20 36V22M28 36V26M36 36V18"/><path d="M10 30l10-8 8 4 12-10"/></svg>
  <p>Search Engine<br>Optimization</p>
</div>
<div class="service" style="left:179px;top:1482px">
  <svg width="52" height="52" viewBox="0 0 52 52" fill="none" stroke="#f05a22" stroke-width="2"><rect x="4" y="8" width="44" height="34" rx="2"/><path d="M4 16h44M10 22h14v12H10zM30 22h12M30 28h12M30 34h8"/></svg>
  <p>Website Design<br>&amp; Development</p>
</div>
<div class="service" style="left:403px;top:1482px">
  <svg width="52" height="52" viewBox="0 0 52 52" fill="none" stroke="#f05a22" stroke-width="2"><circle cx="20" cy="20" r="14"/><path d="M20 12v16M16 16h7a3 3 0 010 6h-6a3 3 0 000 6h7M30 28l4 20 5-8 8-3z"/></svg>
  <p>Pay Per Click<br>(PPC) Management</p>
</div>
<div class="service" style="left:627px;top:1482px">
  <svg width="52" height="52" viewBox="0 0 52 52" fill="none" stroke="#f05a22" stroke-width="2"><rect x="8" y="6" width="36" height="26" rx="2"/><path d="M22 13l10 6-10 6zM4 40h44M12 40v6M40 40v6"/></svg>
  <p>Video Production<br>&amp; Editing</p>
</div>
<div class="service" style="left:851px;top:1482px">
  <svg width="52" height="52" viewBox="0 0 52 52" fill="none" stroke="#f05a22" stroke-width="2"><rect x="6" y="10" width="40" height="30" rx="2"/><path d="M6 18h40M20 24l-5 5 5 5M32 24l5 5-5 5M28 22l-4 14"/></svg>
  <p>Website Hosting &amp;<br>Management</p>
</div>

<div class="btn" style="left:534px;top:1706px;width:132px;height:37px">View All</div>

<!-- FEATURED WORKS -->
<div class="abs featured-band"></div>
<svg class="abs" style="left:1000px;top:1840px" width="200" height="180">
  <rect x="0" y="10" width="200" height="14" fill="#c9401a" opacity=".45"/>
  <rect x="0" y="40" width="200" height="14" fill="#c9401a" opacity=".45"/>
  <rect x="0" y="70" width="200" height="14" fill="#c9401a" opacity=".45"/>
  <rect x="0" y="100" width="200" height="14" fill="#c9401a" opacity=".45"/>
</svg>
<h2 class="section-title" style="left:0;width:1200px;text-align:center;top:1872px;color:var(--white)">FEATURED WORKS</h2>
<p class="lead" style="left:350px;width:500px;top:1932px;color:var(--white)">Apex Reach is a full-service online marketing agency. We can handle any element of your</p>

<div class="work" style="left:91px;top:2010px;width:310px;height:496px;background:linear-gradient(160deg,#f4f4f4,#3fb5d0 45%,#e2367c 80%,#222)" role="img" aria-label="Poster design for a video training course with a camera illustration"></div>
<div class="work" style="left:420px;top:2010px;width:688px;height:239px;background:linear-gradient(135deg,#2a2a2a,#3d3d3d 45%,#d8262c 60%,#eaeaea 80%,#2d2d2d)" role="img" aria-label="Branded stationery mockup with cards and a disc in red, white and black"></div>
<div class="work" style="left:420px;top:2267px;width:310px;height:239px;background:linear-gradient(135deg,#5b5b5b,#3a3a3a)" role="img" aria-label="Website concept sketches on a desk">
  <svg class="abs" style="left:136px;top:80px" width="38" height="38" viewBox="0 0 38 38" fill="none" stroke="#fff" stroke-width="2.5"><path d="M22 4h12v12M34 4L18 20M28 22v12H4V10h12"/></svg>
  <div class="work-caption" style="top:128px;font-size:14px;font-weight:700;text-decoration:underline">WEBSITE</div>
  <div class="work-caption" style="top:148px;font-size:14px">concept for Harper &amp; Lane Law</div>
</div>
<div class="work" style="left:746px;top:2267px;width:362px;height:239px;background:linear-gradient(160deg,#7a2fb0,#9b3fc4 40%,#e08a2a 70%,#c9651d)" role="img" aria-label="Restaurant promotional flyer for a seafood platter"></div>

<div class="divider" style="left:430px;top:2545px;width:447px"></div>
<div class="btn" style="left:534px;top:2590px;width:132px;height:37px">View All</div>

<!-- BLOGS -->
<h2 class="section-title" style="left:174px;top:2697px"><span>OUR</span> BLOGS</h2>

<div class="abs" style="left:457px;top:2775px;width:284px;height:491px;background:var(--white);box-shadow:0 4px 18px rgba(0,0,0,.12)"></div>

<div class="blog-img" style="left:151px;top:2793px;background:linear-gradient(180deg,#4a4a4a,#8b8b8b 55%,#c9c2b8)" role="img" aria-label="Desk with computer monitors in an office"></div>
<div class="blog-img" style="left:472px;top:2793px;background:linear-gradient(135deg,#1e2a3a,#2d4f7a 50%,#1a1a1a)" role="img" aria-label="Smartphone screen showing social media app icons"></div>
<div class="blog-img" style="left:787px;top:2793px;background:linear-gradient(180deg,#e8e8e8,#bdbdbd 60%,#f2f2f2)" role="img" aria-label="Man working at a computer in a bright office"></div>

<h3 class="blog-title" style="left:151px;top:3020px">Search Engine Optimization<br>- Data Analysis</h3>
<h3 class="blog-title" style="left:485px;top:3020px">Business Marketing Strate-<br>gy - Marketing strategy</h3>
<h3 class="blog-title" style="left:787px;top:3020px">Social Media Management -<br>Content creating</h3>

<p class="blog-text" style="left:151px;top:3084px">The SEO playing field is shifting constantly. From week to week, the rules change and your rankings can drop. You need an expert in your corner, helping you navigate</p>
<p class="blog-text" style="left:485px;top:3084px">The SEO playing field is shifting constantly. From week to week, the rules change and your rankings can drop. You need an expert in your ate</p>
<p class="blog-text" style="left:787px;top:3084px">The SEO playing field is shifting constantly. From week to week, the rules change and your rankings can drop. You need an expert in your corner, helping you navigate</p>

<div class="btn btn-outline" style="left:151px;top:3228px;width:133px;height:38px">Read More</div>
<div class="btn" style="left:485px;top:3211px;width:133px;height:38px">Read More</div>
<div class="btn btn-outline" style="left:787px;top:3228px;width:133px;height:38px">Read More</div>

<div class="abs" style="left:569px;top:3334px;width:18px;height:9px;border-radius:5px;background:var(--orange)"></div>
<div class="abs" style="left:598px;top:3334px;width:9px;height:9px;border-radius:50%;background:var(--orange-soft)"></div>
<div class="abs" style="left:618px;top:3334px;width:9px;height:9px;border-radius:50%;background:var(--orange-soft)"></div>

<!-- CONTACT -->
<div class="doodle" style="left:60px;top:3540px;width:200px;height:500px" role="img" aria-label="Line doodles of devices, email and ideas"></div>
<div class="doodle" style="left:950px;top:3540px;width:200px;height:500px" role="img" aria-label="Line doodles of music, a rocket and a phone"></div>

<div class="abs form-box" role="form" aria-label="Send a message">
  <div class="abs" style="inset:0;border-radius:0 70px 70px 70px;background:linear-gradient(180deg,rgba(255,255,255,.06),rgba(0,0,0,.05))" role="img" aria-label="Faint photo of a workspace behind the form"></div>
</div>
<h2 class="abs" style="left:243px;width:714px;top:3464px;text-align:center;font-size:35px;font-weight:400;color:var(--white)">SEND A MESSAGE</h2>

<div class="label" style="left:332px;top:3572px">First name*</div>
<div class="label" style="left:608px;top:3572px">Last name*</div>
<div class="field" style="left:332px;top:3596px;width:260px"></div>
<div class="field" style="left:608px;top:3596px;width:260px"></div>

<div class="label" style="left:332px;top:3670px">Phone number*</div>
<div class="label" style="left:608px;top:3670px">Your e - mail address*</div>
<div class="field" style="left:332px;top:3694px;width:260px"></div>
<div class="field" style="left:608px;top:3694px;width:260px"></div>

<div class="label" style="left:332px;top:3768px">Message*</div>
<div class="field" style="left:332px;top:3792px;width:536px;height:110px"></div>

<div class="btn btn-dark" style="left:534px;top:3963px;width:132px;height:37px">View All</div>

<!-- FOOTER -->
<footer class="abs footer">
  <svg class="abs" style="left:0;top:-22px" width="1200" height="24"><polygon points="0,22 1200,0 1200,24 0,24" fill="#1c1c1c"/></svg>
</footer>
<div class="brand-mark" style="left:583px;top:4215px"></div>
<div class="brand-name" style="left:450px;width:300px;top:4296px;font-size:23px;color:#e9e9e9">APEX REACH</div>
<div class="brand-tag" style="left:450px;width:300px;top:4322px;font-size:15px;color:#cfcfcf">Search Marketing Made Simple</div>

<div class="foot-head" style="left:159px">CONTACT US</div>
<div class="foot-head" style="left:491px">INFORMATION</div>
<div class="foot-head" style="left:668px">USEFUL LINKS</div>
<div class="foot-head" style="left:905px">FOLLOW US</div>

<svg class="abs" style="left:159px;top:4467px" width="16" height="16" viewBox="0 0 24 24"><path d="M6.6 10.8a15 15 0 006.6 6.6l2.2-2.2a1 1 0 011-.25 11.4 11.4 0 003.6.6 1 1 0 011 1V20a1 1 0 01-1 1A17 17 0 013 4a1 1 0 011-1h3.5a1 1 0 011 1c0 1.250.2 2.450.6 3.6a1 1 0 01-.25 1z" fill="#f05a22"/></svg>
<div class="foot-link" style="left:191px;top:4466px;color:var(--orange);font-size:15px">800-555-0142</div>
<svg class="abs" style="left:159px;top:4505px" width="16" height="13" viewBox="0 0 16 13"><rect x="0" y="0" width="16" height="13" rx="1" fill="#bdbdbd"/><path d="M1 1l7 6 7-6" stroke="#1c1c1c" stroke-width="1.4" fill="none"/></svg>
<div class="foot-link" style="left:191px;top:4503px">hello@apexreach.com</div>
<svg class="abs" style="left:160px;top:4539px" width="13" height="18" viewBox="0 0 13 18"><path d="M6.5 0A6.5 6.5 0 000 6.5C0 11 6.5 18 6.5 18S13 11 13 6.5A6.5 6.5 0 006.5 0z" fill="#bdbdbd"/><circle cx="6.5" cy="6.5" r="2.4" fill="#1c1c1c"/></svg>
<div class="foot-link" style="left:191px;top:4539px;line-height:18px">Northbay Supply, LLC<br>410 Harbor Lane<br>Lakeview, FL 32000</div>

<div class="foot-link" style="left:491px;top:4468px">Home</div>
<div class="foot-link" style="left:491px;top:4505px">About</div>
<div class="foot-link" style="left:491px;top:4542px">Services</div>
<div class="foot-link" style="left:491px;top:4578px">Blog</div>
<div class="foot-link" style="left:491px;top:4615px">Contact</div>

<div class="foot-link" style="left:668px;top:4468px">Copy Rights</div>
<div class="foot-link" style="left:668px;top:4505px">Terms &amp; condition</div>
<div class="foot-link" style="left:668px;top:4542px">Privacy Policy</div>

<div class="social" style="left:903px;top:4470px;border-color:#bdbdbd"></div>
<div class="social" style="left:949px;top:4470px;border-color:#bdbdbd"></div>
<div class="social" style="left:995px;top:4470px;border-color:#bdbdbd"></div>
<div class="social" style="left:1041px;top:4470px;border-color:#bdbdbd"></div>

<div class="abs" style="left:0;top:4712px;width:1200px;height:1px;background:#333"></div>
<p class="abs" style="right:90px;top:4744px;font-size:14px;color:#e6e6e6">COPYRIGHT © 2020 <span style="color:var(--orange)">Apex Reach LLC. All Rights Reserved.</span></p>

</body>
</html>
```